Miriams Professional Resume

Pls upgrade to make look more effective and perhaps add α photo on it, both options with photo and without would be great. Thanks very much. I would also like the resume so I can edit as well if I need to down the track.

Target Market(s)

This is my professional resume to make it more effective to potential senior hiring managers,

Colors
f04a50

Requirements
Must have
• Professional look.

```html
<!DOCTYPE html>
<html lang="en">
<head>
<meta charset="UTF-8">
<title>Miriam Dalton – Resume</title>
<link href="https://fonts.googleapis.com/css2?family=Montserrat:wght@300;400;500;600;700&display=swap" rel="stylesheet">
<style>
  :root{
    --accent:#0099d3;
    --ink:#111111;
    --panel:#f3f3f3;
    --track:#bdbdbd;
    --white:#ffffff;
  }
  *{margin:0;padding:0;box-sizing:border-box;}
  html,body{width:849px;height:1200px;overflow:hidden;background:var(--white);}
  body{font-family:'Montserrat',sans-serif;color:var(--ink);}
  .resume{position:relative;width:849px;height:1200px;overflow:hidden;background:var(--white);}
  .abs{position:absolute;}

  .side-band{left:0;top:32px;width:31px;height:189px;background:var(--accent);}
  .contact-panel{left:541px;top:32px;width:308px;height:189px;background:var(--accent);}
  .side-panel{left:541px;top:221px;width:308px;height:979px;background:var(--panel);}

  .portrait{left:51px;top:39px;width:176px;height:176px;border-radius:50%;
    background:radial-gradient(circle at 50% 40%,#e9d6cf 0%,#c7a9a2 45%,#6b4a4c 75%,#d9dcdf 100%);
    border:1px solid #e4e4e4;}

  .name{left:246px;top:63px;font-weight:700;font-size:38px;line-height:45px;letter-spacing:5.5px;}
  .role{left:246px;top:154px;font-weight:300;font-size:23px;line-height:28px;}

  .contact{right:76px;color:var(--white);font-weight:500;font-size:13.6px;line-height:18px;text-align:right;white-space:nowrap;}
  .contact.link{text-decoration:underline;}
  .contact-icon{left:787px;width:32px;height:32px;}

  .heading{font-weight:700;font-size:15.5px;line-height:20px;white-space:nowrap;}
  .heading-bar{height:4.5px;width:61px;background:var(--accent);}

  .entry-date{left:42px;font-weight:700;font-size:14px;line-height:20px;white-space:nowrap;}
  .entry{font-size:13px;line-height:17px;}
  .entry .title{font-weight:700;font-size:15.5px;line-height:19px;}
  .entry .detail{font-weight:400;}
  .entry.edu{font-size:14px;line-height:19px;}
  .entry.edu .title{font-size:14.3px;line-height:19px;}

  .statement{left:564px;top:274px;width:243px;font-size:12.6px;line-height:16.95px;text-align:justify;}

  .skill{left:564px;font-size:14.3px;line-height:18px;}
  .skill-track{left:699px;width:119px;height:5px;background:var(--track);}
  .skill-fill{position:absolute;left:0;top:0;height:100%;width:91px;background:var(--accent);}

  .member{left:566px;font-size:15.5px;line-height:20.5px;}
  .member .org{font-weight:700;}
  .member .num{font-weight:400;padding-left:4px;line-height:22px;}

  .course{left:42px;font-size:14.2px;line-height:19px;}
  .course .title{font-weight:700;}
  .course .detail{font-weight:400;font-size:14px;}
</style>
</head>
<body>
<div class="resume">
  <div class="abs side-band"></div>
  <div class="abs contact-panel"></div>
  <div class="abs side-panel"></div>

  <div class="abs portrait" role="img" aria-label="Portrait photo of Miriam Dalton"></div>

  <div class="abs name">MIRIAM<br>DALTON</div>
  <div class="abs role">Senior Manager</div>

  <div class="abs contact" style="top:78px;">098761234</div>
  <div class="abs contact" style="top:116px;">miriamd@daltonadvisory.com</div>
  <div class="abs contact link" style="top:153px;">miriam-dalton-7c3b10482</div>

  <svg class="abs contact-icon" style="top:64px;" viewBox="0 0 32 32" fill="none" stroke="#fff" stroke-width="1.6" stroke-linejoin="round" stroke-linecap="round" aria-hidden="true">
    <path d="M6 5l5-1 3 7-3 2c1.5 3.5 4 6 7.5 7.5l2-3 7 3-1 5c-11 1-21-9-20.5-20.5z"/>
    <path d="M18 4a10 10 0 0 1 10 10"/><path d="M18 8a6 6 0 0 1 6 6"/>
  </svg>
  <svg class="abs contact-icon" style="top:107px;" viewBox="0 0 32 32" fill="none" stroke="#fff" stroke-width="1.6" stroke-linejoin="round" aria-hidden="true">
    <rect x="2" y="6" width="28" height="20"/><path d="M2 6l14 12 14-12M2 26l10-10M30 26L20 16"/>
  </svg>
  <svg class="abs contact-icon" style="top:150px;" viewBox="0 0 32 32" fill="none" stroke="#fff" stroke-width="1.6" aria-hidden="true">
    <circle cx="16" cy="16" r="14"/>
  </svg>

  <!-- Career -->
  <div class="abs heading" style="left:42px;top:241px;">CAREER HISTORY:</div>
  <div class="abs heading-bar" style="left:43px;top:263px;"></div>

  <div class="abs entry-date" style="top:275px;">Aug 2015 - Present</div>
  <div class="abs entry" style="left:208px;top:275px;">
    <div class="title">Senior Manager</div>
    <div class="detail">Organisational Development Director, Service,<br>&nbsp;FMCG Industry Dalton Advisory Group<br>&nbsp;Singapore</div>
  </div>

  <div class="abs entry-date" style="top:366px;">Jun 2008 – Aug 2015</div>
  <div class="abs entry" style="left:208px;top:366px;">
    <div class="title">Organisational Development Director<br>Client Relations</div>
    <div class="detail">&nbsp;Brightwell Pty. Ltd.,<br>&nbsp;Australia</div>
  </div>

  <div class="abs entry-date" style="top:455px;">Oct 2003 – Dec 2007</div>
  <div class="abs entry" style="left:206px;top:455px;">
    <div class="title">Director Career Services</div>
    <div class="detail" style="font-size:14px;">&nbsp;Northgate College<br>&nbsp;USA</div>
  </div>

  <!-- Education -->
  <div class="abs heading" style="left:42px;top:594px;">EDUCATION:</div>
  <div class="abs heading-bar" style="left:43px;top:615px;"></div>

  <div class="abs entry-date" style="top:627px;">Dec 2011- Dec 2017</div>
  <div class="abs entry edu" style="left:208px;top:627px;">
    <div class="title">Masters in Strategic Organisational<br>Development</div>
    <div class="detail">University of Eastfield<br>Australia</div>
  </div>

  <div class="abs entry-date" style="left:45px;top:718px;">Jun 2003- Nov 2006</div>
  <div class="abs entry edu" style="left:205px;top:718px;">
    <div class="title">Management in Human Resources<br>Certificate – Graduated with Distinction</div>
    <div class="detail">Westmoor University Extension<br>&nbsp;Program, USA</div>
  </div>

  <div class="abs entry-date" style="left:45px;top:829px;">Jan 1992- Dec 1996</div>
  <div class="abs entry edu" style="left:204px;top:829px;">
    <div class="title">Bachelor of Business in Tourism<br>Management</div>
    <div class="detail">Coral Coast University,Australia</div>
  </div>

  <!-- Courses -->
  <div class="abs heading" style="left:42px;top:967px;">CURRENT COURSES COMPLETED:</div>
  <div class="abs heading-bar" style="left:43px;top:988px;"></div>

  <div class="abs course" style="top:1013px;">
    <div class="title">Singapore Employment Legislation and Industrial Relations</div>
    <div class="detail">SPPI, 2020.</div>
  </div>
  <div class="abs course" style="top:1092px;">
    <div class="title">Human Resource Analytics and Insights</div>
    <div class="detail">SPPI, 2020.</div>
  </div>

  <!-- Side panel -->
  <div class="abs heading" style="left:564px;top:234px;">PROFESSIONAL STATEMENT:</div>
  <div class="abs heading-bar" style="left:564px;top:257px;"></div>
  <p class="abs statement">My strength is in leadership, developing strategies and providing excellence in HR Operational Services, Recruiting, People Development and building high performing teams to accelerate business performance and drive engagement. Masters in Strategic Organisational Development. As an authentic leader I excel at navigating across the business to build a positive culture while consulting with executives to understand imperative business needs and recommend the best solution. Successfully rolled out Fizzwell Project for 200 + new customer sites for the Orchard Pure Fruit Project and actively recruited for 20 + technical field service agents, developed their capabilities and achieved 100 % completion of the project.</p>

  <div class="abs heading" style="left:563px;top:655px;">PERSONAL SKILLS:</div>
  <div class="abs heading-bar" style="left:563px;top:678px;"></div>

  <div class="abs skill" style="top:702px;">TEAM WORK</div>
  <div class="abs skill-track" style="top:705px;"><div class="skill-fill"></div></div>
  <div class="abs skill" style="top:739px;">COMMUNICATION</div>
  <div class="abs skill-track" style="top:742px;"><div class="skill-fill"></div></div>
  <div class="abs skill" style="top:777px;">ORGANIZATION</div>
  <div class="abs skill-track" style="top:781px;"><div class="skill-fill"></div></div>
  <div class="abs skill" style="top:814px;">LEADERSHIP</div>
  <div class="abs skill-track" style="top:816px;"><div class="skill-fill"></div></div>
  <div class="abs skill" style="top:852px;">TEAMPLAYER</div>
  <div class="abs skill-track" style="top:854px;"><div class="skill-fill"></div></div>

  <div class="abs heading" style="left:564px;top:932px;">PROFESSIONAL MEMBERSHIP:</div>
  <div class="abs heading-bar" style="left:564px;top:960px;"></div>

  <div class="abs member" style="top:994px;">
    <div class="org">Member of Singapore People<br>Practice Institute ,</div>
    <div class="num">208 4571 3031</div>
  </div>
  <div class="abs member" style="top:1088px;">
    <div class="org">Member of Australian Workforce<br>Institute,</div>
    <div class="num">582316.</div>
  </div>
</div>
</body>
</html>
```